まず、縦を想定しており、画像をメインにした構成を想定しております。

上半分は覚悟を決めた中年以上の料理にが仁王立ちしているようなイメージの写真で「店を売るという選択」or「店をゆずる決断」というキャプション

下半分はやる気に満ち溢れた若者が覚悟を持って仁王立ちしているようなイメージ
「店を買う」or「店(歴史)を引きつぐ覚悟」というキャプション

そして、下の方に計算式添付の資料にあるような表を挿入。
売却した方は結局、いくら得したのか。買った方はいくら得したのかがわかるように。あとは、「査定無料」「神奈川エリアに特化した唯一のエージェントです」を記載お願いします。最後にヴェルコハーバーズという社名と連絡先を記載。

全体的なイメージではノルヴェクや外国の広告のようにシンプルだけどもどこかデザイン性を感じるように。また、信頼性も大事なので全体的にシックだけども目を引くように。
VELKO HARBORS
ヴェルコハーバーズ
0120-471-362
www.velko-harbors-jp.example
A4
片面
青系、茶系、グレー系
• 高解像度JPG (.jpg)
• イラストレーター形式 (.ai)
キャプションの修正
【メインキャプション】大事なお店、最も高く売却いたします。
【売手側キャプション】 お店を売るという選択
【買手側キャプション】お店を買うという選択

また、各キャプションを大きめに表示をお願いします。

全体的にまとまっており、柔軟に対応頂いたため。

ありがとうござました!!

```html
<!DOCTYPE html>
<html lang="ja">
<head>
<meta charset="utf-8">
<title>ヴェルコハーバーズ 店舗売買</title>
<link rel="stylesheet" href="https://fonts.googleapis.com/css2?family=Noto+Serif+JP:wght@500;700;900&family=Noto+Sans+JP:wght@400;500;700&display=swap">
<style>
:root{
  --ink:#2b2622;
  --bg-dark:#3a3531;
  --bg-mid:#6d6660;
  --bg-light:#a9a39c;
  --brown:#7a4a2c;
  --brown-deep:#5a3520;
  --blue:#2f4f73;
  --blue-deep:#1f3857;
  --gray-panel:#e6e4e1;
  --paper:#ffffff;
  --line:#c8c3bd;
  --accent-red:#b0312a;
}
*{margin:0;padding:0;box-sizing:border-box}
html,body{width:846px;height:1200px;overflow:hidden;background:var(--paper)}
body{font-family:"Noto Sans JP",sans-serif;color:var(--ink);position:relative}
.hero{position:absolute;left:0;top:0;width:846px;height:950px;
  background:radial-gradient(ellipse at 50% 35%,var(--bg-light) 0%,var(--bg-mid) 45%,var(--bg-dark) 100%)}
.hero-photo{position:absolute;left:0;top:40px;width:846px;height:625px;
  background:linear-gradient(90deg,rgba(240,236,230,.18) 0%,rgba(240,236,230,.05) 40%,rgba(240,236,230,.05) 60%,rgba(240,236,230,.18) 100%)}
.top-strip{position:absolute;left:0;top:0;width:846px;height:40px;display:flex;align-items:center;padding-left:20px;gap:12px}
.badge-free{background:var(--accent-red);color:#fff;font-size:12px;font-weight:700;padding:4px 9px}
.tagline{color:#fff;font-size:13px;letter-spacing:.04em}
.brand-top{position:absolute;right:28px;top:34px;display:flex;flex-direction:column;align-items:center;gap:4px;color:#fff}
.brand-top .mark{width:34px;height:34px;background:var(--brown)}
.brand-top .en{font-size:14px;font-weight:700;letter-spacing:.08em}
.brand-top .jp{font-size:10px;letter-spacing:.1em}
.headline{position:absolute;left:250px;top:60px;height:610px;writing-mode:vertical-rl;
  font-family:"Noto Serif JP",serif;font-weight:900;color:#fff;display:flex;gap:14px;
  text-shadow:0 2px 8px rgba(0,0,0,.35)}
.headline .l1{font-size:80px;line-height:1}
.headline .l2{font-size:50px;line-height:1;padding-top:84px}
.choice{position:absolute;top:665px;width:420px}
.choice.sell{left:0}
.choice.buy{right:0}
.caption{height:44px;display:flex;align-items:center;padding-left:22px;color:#fff;
  font-family:"Noto Serif JP",serif;font-weight:700;font-size:23px;letter-spacing:.04em}
.sell .caption{background:linear-gradient(90deg,var(--brown-deep),var(--brown))}
.buy .caption{background:linear-gradient(90deg,var(--blue-deep),var(--blue))}
.merit{position:absolute;top:-30px;width:88px;height:88px;border-radius:50%;background:#fff;
  display:flex;flex-direction:column;align-items:center;justify-content:center;font-weight:700;line-height:1.2}
.sell .merit{right:36px;color:var(--brown);border:3px solid var(--brown)}
.buy .merit{left:6px;color:var(--blue);border:3px solid var(--blue)}
.merit .big{font-size:16px}
.merit .small{font-size:11px}
.sim{margin:12px 16px 0 16px;width:388px;border-collapse:collapse;font-size:11px;background:var(--paper)}
.sim caption{text-align:left;font-weight:700;font-size:12px;color:#fff;padding:5px 8px;caption-side:top}
.sell .sim caption{background:var(--brown-deep)}
.buy .sim caption{background:var(--blue-deep)}
.sim th,.sim td{border-bottom:1px solid var(--line);padding:7px 8px}
.sim thead th{font-weight:500;color:#555;background:var(--gray-panel);text-align:right}
.sim thead th:first-child{text-align:left}
.sim tbody th{text-align:left;font-weight:500}
.sim td{text-align:right}
.sim td.ours{font-weight:700}
.sell .sim td.ours{color:var(--brown)}
.buy .sim td.ours{color:var(--blue)}
.sim tr.total th,.sim tr.total td{font-weight:700;border-bottom:2px solid var(--ink)}
.lower{position:absolute;left:0;top:950px;width:846px;height:250px;background:var(--paper)}
.explain{text-align:center;font-size:14px;line-height:1.75;color:var(--ink);padding-top:22px}
.brand-bottom{display:flex;flex-direction:column;align-items:center;gap:4px;margin-top:16px}
.brand-bottom .mark{width:26px;height:26px;background:var(--blue)}
.brand-bottom .en{font-size:14px;font-weight:700;letter-spacing:.1em;color:var(--ink)}
.footer{position:absolute;left:0;bottom:0;width:846px;height:44px;border-top:1px solid var(--line);
  display:flex;align-items:center;justify-content:space-between;padding:0 34px;font-size:13px}
.footer .name{font-weight:700;letter-spacing:.06em}
.footer .tel{display:flex;align-items:center;gap:6px;font-weight:700;font-size:16px}
</style>
</head>
<body>
<section class="hero">
  <div class="hero-photo" role="img" aria-label="年配の料理人と若い料理人が白いコック服で並んで堂々と立つ写真"></div>
  <div class="top-strip">
    <span class="badge-free">査定無料</span>
    <span class="tagline">神奈川エリアに特化した唯一のエージェントです</span>
  </div>
  <div class="brand-top">
    <span class="mark"></span>
    <span class="en">VELKO HARBORS</span>
    <span class="jp">ヴェルコハーバーズ</span>
  </div>
  <h1 class="headline"><span class="l1">大事なお店、</span><span class="l2">最も高く売却いたします。</span></h1>

  <div class="choice sell">
    <div class="caption">お店を売るという選択</div>
    <div class="merit"><span class="big">300万円</span><span class="small">のメリット</span></div>
    <table class="sim">
      <caption>退店コストシミュレーション</caption>
      <thead><tr><th></th><th>通常退店</th><th>弊社サービス</th></tr></thead>
      <tbody>
        <tr><th>解約時の修繕</th><td>▲500,000円</td><td class="ours">0円</td></tr>
        <tr><th>内装解体費用</th><td>▲500,000円</td><td class="ours">0円</td></tr>
        <tr><th>造作売買代金</th><td>0円</td><td class="ours">2,000,000円</td></tr>
        <tr class="total"><th>計</th><td>▲1,000,000円</td><td class="ours">2,000,000円</td></tr>
      </tbody>
    </table>
  </div>

  <div class="choice buy">
    <div class="caption" style="padding-left:110px">お店を買うという選択</div>
    <div class="merit"><span class="big">950万円</span><span class="small">のコストダウン</span></div>
    <table class="sim">
      <caption>出店コストシミュレーション</caption>
      <thead><tr><th></th><th>通常出店</th><th>弊社サービス</th></tr></thead>
      <tbody>
        <tr><th>内装設備工事費</th><td>13,000,000円</td><td class="ours">0円</td></tr>
        <tr><th>造作売買代金</th><td>0円</td><td class="ours">3,500,000円</td></tr>
        <tr class="total"><th>計</th><td>13,000,000円</td><td class="ours">3,500,000円</td></tr>
      </tbody>
    </table>
  </div>
</section>

<section class="lower">
  <p class="explain">通常、解約申請から実際の退去までには多くの支払いが発生します。<br>
  お店を売却する事が出来れば、手元に現金を残して退去できます。<br>
  また、買取された方も費用を抑えて出店が出来るため双方にメリットがでる仕組みになっております。</p>
  <div class="brand-bottom">
    <span class="mark"></span>
    <span class="en">VELKO HARBORS</span>
  </div>
  <div class="footer">
    <span class="name">VELKO HARBORS　ヴェルコハーバーズ</span>
    <span class="tel">
      <svg width="18" height="18" viewBox="0 0 24 24" aria-hidden="true"><path fill="currentColor" d="M6.6 10.8a15.1 15.1 0 0 0 6.6 6.6l2.2-2.2c.3-.3.7-.4 1-.2 1.1.4 2.3.6 3.6.6.6 0 1 .4 1 1V20c0 .6-.4 1-1 1A17 17 0 0 1 3 4c0-.6.4-1 1-1h3.5c.6 0 1 .4 1 1 0 1.3.2 2.5.6 3.6.1.3 0 .7-.2 1z"/></svg>
      0120-471-362
    </span>
    <span class="url">www.velko-harbors-jp.example</span>
  </div>
</section>
</body>
</html>
```